The calm within me tour 2019

I need an improvement of my own design for a speaking tour on shame and mental health. The advertisement will be for social media. I would like someone to remove the background and do something creative and contemporary. My preference is just my head and shoulders.

Target Market(s)

Church pastors and leaders of mental health organisations

Industry/Entity Type

Mental Health

Requirements
Must have
• The same wording as original
• Delete background and replace with something that is simple but funky

```html
<!DOCTYPE html>
<html lang="en">
<head>
<meta charset="utf-8">
<title>The Calm Within Me Tour 2019 – Social Ads</title>
<link rel="stylesheet" href="https://fonts.googleapis.com/css2?family=Montserrat:wght@400;700&display=swap">
<style>
  :root {
    --page-bg: #1b1b1b;
    --headline-blue: #4f86f7;
    --headline-grey: #6d6d6d;
    --name-grey: #7a7a7a;
    --grey-light: #ffffff;
    --grey-mid: #d9d9d9;
    --grey-deep: #8c8c8c;
    --blue-light: #ffffff;
    --blue-mid: #9fd3ee;
    --blue-deep: #1f86d6;
  }
  * { box-sizing: border-box; margin: 0; padding: 0; }
  html, body {
    width: 742px;
    height: 1200px;
    overflow: hidden;
    background: var(--page-bg);
    font-family: "Montserrat", Arial, sans-serif;
  }
  .ad {
    position: absolute;
    left: 35px;
    width: 672px;
    height: 543px;
    overflow: hidden;
  }
  .ad--grey {
    top: 56px;
    background: linear-gradient(105deg, var(--grey-light) 0%, var(--grey-light) 30%, var(--grey-mid) 55%, var(--grey-deep) 100%);
  }
  .ad--blue {
    top: 614px;
    background: linear-gradient(105deg, var(--blue-light) 0%, var(--blue-light) 28%, var(--blue-mid) 55%, var(--blue-deep) 100%);
  }
  .ad__planes {
    position: absolute;
    inset: 0;
    width: 100%;
    height: 100%;
  }
  .ad__portrait {
    position: absolute;
    left: 300px;
    top: 28px;
    width: 372px;
    height: 515px;
    border-radius: 150px 150px 0 0;
  }
  .ad--grey .ad__portrait { background: linear-gradient(180deg, #6b5f57 0%, #8a7466 40%, #2a2624 70%, #151515 100%); }
  .ad--blue .ad__portrait { background: linear-gradient(180deg, #5e5e5e 0%, #8a8a8a 40%, #2b2b2b 70%, #151515 100%); }
  .headline { position: absolute; left: 43px; top: 0; }
  .headline__line {
    position: absolute;
    left: 0;
    line-height: 1;
    white-space: nowrap;
  }
  .headline__line--lead { top: 94px; font-size: 46px; font-weight: 400; color: var(--headline-grey); }
  .headline__line--key  { top: 152px; font-size: 62px; font-weight: 700; color: var(--headline-blue); }
  .headline__line--sub  { top: 222px; font-size: 40px; font-weight: 700; color: var(--headline-blue); }
  .headline__line--tail { top: 268px; font-size: 46px; font-weight: 400; color: var(--headline-grey); }
  .speaker {
    position: absolute;
    left: 43px;
    top: 440px;
    display: flex;
    align-items: center;
    gap: 10px;
  }
  .speaker__mark {
    width: 22px;
    height: 22px;
    background: var(--headline-blue);
  }
  .speaker__name {
    font-size: 24px;
    font-weight: 400;
    color: var(--name-grey);
    line-height: 1;
  }
</style>
</head>
<body>

<section class="ad ad--grey">
  <svg class="ad__planes" viewBox="0 0 672 543" aria-hidden="true">
    <polygon points="420,0 672,0 672,300" fill="#a6a6a6" opacity="0.35"/>
    <polygon points="250,543 470,200 520,543" fill="#bdbdbd" opacity="0.35"/>
  </svg>
  <div class="ad__portrait" role="img" aria-label="Head-and-shoulders portrait of the speaker in a black V-neck t-shirt"></div>
  <h1 class="headline">
    <span class="headline__line headline__line--lead">THE</span>
    <span class="headline__line headline__line--key">CALM</span>
    <span class="headline__line headline__line--sub">WITHIN ME</span>
    <span class="headline__line headline__line--tail">TOUR 2019</span>
  </h1>
  <div class="speaker">
    <span class="speaker__mark"></span>
    <span class="speaker__name">ned calloway</span>
  </div>
</section>

<section class="ad ad--blue">
  <svg class="ad__planes" viewBox="0 0 672 543" aria-hidden="true">
    <polygon points="120,0 500,0 380,230" fill="#cfeaf6" opacity="0.5"/>
    <polygon points="250,543 470,180 540,543" fill="#6fb7e6" opacity="0.4"/>
    <polygon points="560,0 672,0 672,420" fill="#1479c8" opacity="0.35"/>
  </svg>
  <div class="ad__portrait" role="img" aria-label="Black-and-white head-and-shoulders portrait of the speaker in a black V-neck t-shirt"></div>
  <h1 class="headline">
    <span class="headline__line headline__line--lead">THE</span>
    <span class="headline__line headline__line--key">CALM</span>
    <span class="headline__line headline__line--sub">WITHIN ME</span>
    <span class="headline__line headline__line--tail">TOUR 2019</span>
  </h1>
  <div class="speaker">
    <span class="speaker__mark"></span>
    <span class="speaker__name">ned calloway</span>
  </div>
</section>

</body>
</html>
```